Flyer-Design für Konzertflyer gemischter Chor
Zielgruppe
Wir, die Klangfreunde Wellbach sind ein gemischter Chor aus der Schweiz. Für unser nächstes Konzert mit dem Titel ' Lieder zum Träumen' brauchen wir einen Flyer der auf den Anlass Aufmerksam macht.
Näheres zum Chor auf unserer Website www.klangfreunde-wellbach.ch.
Aufgabenstellung
Mit dem Titel sind nicht nur Lieder zum verlieben gemeint sondern auch Songs in die man sich verlieben kann oder die einem an etwas schönes Erinnern. Wir denken da an ein stimmungsvolles Design mit nicht nur roten Herzen.
Programmausschnitt: Winds across the silver bay , Harlan Moody / Lanterns in the rain / Kima Soro / Walk beside the quiet river tonight, Garth Wells / Paper boats at dusk, Russ Tanner / Tidal hymn, Trevor Halloway / Brightwater, Harbor lane tales / Bells over meadows , Cedar hall
Format: A5 hochkant.
Text: "Lieder zum Träumen" Konzert Klangfreunde Wellbach.
Samstag 19. November 17.00 Uhr, Uerikon/Stäfa, Singsaal Lindenhain
Sonntag 20. November 17.00Uhr, Uetikon am See, Kornblumsaal
Eintritt frei Kollekte
www.klangfreunde-wellbach.ch

```html
<!DOCTYPE html>
<html lang="de">
<head>
<meta charset="utf-8">
<title>Lieder zum Träumen – Konzert Klangfreunde Wellbach</title>
<link rel="stylesheet" href="https://fonts.googleapis.com/css2?family=Barlow:ital,wght@0,500;0,600;0,700;1,800;1,900&display=swap">
<style>
  :root {
    --stage: #d9d9d9;
    --paper: #ffffff;
    --title-red: #d9202b;
    --art-red: #e0473a;
    --art-soft: #f6c3b9;
    --magenta: #c4128c;
    --ink: #222222;
  }
  * { margin: 0; padding: 0; box-sizing: border-box; }
  html, body {
    width: 1200px; height: 1200px; overflow: hidden;
    background: var(--stage);
    font-family: "Barlow", Arial, sans-serif;
  }
  .flyer {
    position: absolute; left: 211px; top: 50px;
    width: 778px; height: 1100px;
    background: var(--paper);
    overflow: hidden;
  }
  .artwork {
    position: absolute; left: 0; top: 0; width: 778px; height: 700px;
    background: radial-gradient(ellipse 62% 58% at 50% 45%,
      var(--paper) 0%, var(--art-soft) 45%, var(--art-red) 72%, var(--art-soft) 88%, var(--paper) 100%);
  }
  .title {
    position: absolute; left: 0; top: 175px; width: 778px;
    color: var(--title-red);
    font-weight: 900; font-style: italic; text-transform: uppercase;
    line-height: 1;
  }
  .title-line { display: block; font-size: 96px; letter-spacing: 1px; }
  .title-line.first { padding-left: 170px; }
  .title-line.second { padding-left: 182px; }
  .title-small { font-size: 34px; letter-spacing: 1px; }
  .choir-banner {
    position: absolute; left: 180px; top: 392px;
    background: var(--magenta); color: var(--paper);
    font-weight: 700; font-size: 27px;
    padding: 8px 20px;
    transform: rotate(-3deg);
  }
  .entry-badge {
    position: absolute; left: 585px; top: 428px;
    width: 160px; height: 160px; border-radius: 50%;
    background: var(--magenta); color: var(--paper);
    display: flex; align-items: center; justify-content: center; text-align: center;
    font-weight: 700; font-size: 21px; line-height: 1.25;
    transform: rotate(10deg);
  }
  .dates {
    position: absolute; left: 0; top: 720px; width: 778px;
    text-align: center; color: var(--ink);
  }
  .date-heading {
    color: var(--title-red);
    font-weight: 900; font-style: italic; text-transform: uppercase;
    font-size: 66px; line-height: 1;
  }
  .date-heading .date-number { font-size: 54px; }
  .date-detail { font-size: 25px; font-weight: 500; line-height: 1.35; }
  .date-block + .date-block { margin-top: 20px; }
  .date-block .date-detail:first-of-type { margin-top: 8px; }
  .website {
    position: absolute; left: 0; top: 1040px; width: 778px;
    text-align: center; font-weight: 700; font-size: 28px; color: var(--ink);
  }
</style>
</head>
<body>
  <main class="flyer">
    <div class="artwork" role="img" aria-label="Illustration: rotes Herz, umrahmt von einem Wirbel aus roten Musiknoten"></div>

    <h1 class="title">
      <span class="title-line first">Lieder <span class="title-small">zum</span></span>
      <span class="title-line second">Träumen</span>
    </h1>

    <div class="choir-banner">Konzert Klangfreunde Wellbach</div>
    <div class="entry-badge">Eintritt frei –<br>Kollekte</div>

    <section class="dates">
      <div class="date-block">
        <h2 class="date-heading">Samstag <span class="date-number">19. Nov. 2016</span></h2>
        <p class="date-detail">17.00 Uhr · Uerikon/Stäfa</p>
        <p class="date-detail">Singsaal Schulhaus Lindenhain</p>
      </div>
      <div class="date-block">
        <h2 class="date-heading">Sonntag <span class="date-number">20. Nov. 2016</span></h2>
        <p class="date-detail">17.00 Uhr · Uetikon am See</p>
        <p class="date-detail">Kornblumsaal</p>
      </div>
    </section>

    <p class="website">www.klangfreunde-wellbach.ch</p>
  </main>
</body>
</html>
```